Quarnfield Fintech Product Infographic

Quarnfield is an established Fintech business, supplying complex financial software to banks and building societies.

We currently have a picture/infographic to show each of our 11 different software products in a single image. Each product can be installed on its own as a standalone application or if multiple products are installed they will share data.

The key message for our infographic is to convey the integration via a shared database.

The attached diagram is what we currently use which is to give you an idea of the message we are trying to give, but we are not tied to this format and are looking for this diagram to be reimagined.

We will look to use our new chosen design on printed media such as A4 Data sheets an example of which is attached.

For more information on our products please refer to www.quarnfield-example.co.uk/products

```html
<!DOCTYPE html>
<html lang="en">
<head>
<meta charset="utf-8">
<title>Quarnfield – Shared Data Product Infographic</title>
<link rel="stylesheet" href="https://fonts.googleapis.com/css2?family=Montserrat:wght@600;700;800&display=swap">
<style>
  :root {
    --page-grey: #e4e4e6;
    --card-white: #ffffff;
    --purple: #b775b5;
    --orange: #f8b54a;
    --green: #5dbd84;
    --sky: #41b4e7;
    --navy: #1b2e6c;
    --core-light: #2f7fcc;
    --core-dark: #142c6b;
    --hub-light: #d9eefb;
    --hub-edge: #5ab8ea;
    --ink: #111111;
  }
  html, body {
    margin: 0;
    padding: 0;
    width: 1200px;
    height: 884px;
    overflow: hidden;
    background: var(--page-grey);
  }
  .infographic {
    display: block;
    width: 1200px;
    height: 884px;
    font-family: "Montserrat", Arial, sans-serif;
  }
  .card { fill: var(--card-white); }
  .arc { fill: none; }
  .arc--purple { stroke: var(--purple); }
  .arc--orange { stroke: var(--orange); }
  .arc--green { stroke: var(--green); }
  .arc--sky { stroke: var(--sky); }
  .arc-label {
    fill: #ffffff;
    font-weight: 700;
    font-size: 18px;
    letter-spacing: 0.2px;
    text-anchor: middle;
  }
  .module-core { fill: url(#coreGradient); stroke: #ffffff; stroke-width: 7; }
  .module-title {
    fill: #ffffff;
    font-weight: 800;
    font-size: 31px;
    text-anchor: middle;
    letter-spacing: 0.5px;
  }
  .icon-stroke { fill: none; stroke: #ffffff; stroke-width: 6; stroke-linecap: round; stroke-linejoin: round; }
  .icon-fill { fill: #ffffff; }
  .icon-cut { fill: var(--core-light); }
  .connector-line { stroke: var(--sky); stroke-width: 4; }
  .connector-dot { fill: #ffffff; stroke-width: 3; }
  .hub-ring { fill: #ffffff; stroke: var(--navy); stroke-width: 4; }
  .hub-dots { fill: none; stroke: var(--orange); stroke-width: 2; stroke-dasharray: 1 5; stroke-linecap: round; }
  .hub-core { fill: url(#hubGradient); }
  .hub-title {
    fill: var(--ink);
    font-weight: 800;
    font-size: 46px;
    text-anchor: middle;
    letter-spacing: 0.5px;
  }
  .exchange-mark { fill: var(--ink); }
</style>
</head>
<body>
<svg class="infographic" viewBox="0 0 1200 884" xmlns="http://www.w3.org/2000/svg">
  <defs>
    <radialGradient id="coreGradient" cx="50%" cy="40%" r="60%">
      <stop offset="0" stop-color="var(--core-light)"/>
      <stop offset="1" stop-color="var(--core-dark)"/>
    </radialGradient>
    <radialGradient id="hubGradient" cx="50%" cy="35%" r="65%">
      <stop offset="0" stop-color="var(--hub-light)"/>
      <stop offset="1" stop-color="var(--hub-edge)"/>
    </radialGradient>
    <filter id="softShadow" x="-20%" y="-20%" width="140%" height="140%">
      <feDropShadow dx="0" dy="6" stdDeviation="7" flood-color="#0b2350" flood-opacity="0.35"/>
    </filter>

    <!-- label guides: each runs from the left point, mid-point sits at the right point -->
    <path id="perfCw143" d="M115 268 a143 143 0 1 1 286 0 a143 143 0 1 1 -286 0"/>
    <path id="perfCw142" d="M116 268 a142 142 0 1 1 284 0 a142 142 0 1 1 -284 0"/>
    <path id="perfCcw139" d="M119 268 a139 139 0 1 0 278 0 a139 139 0 1 0 -278 0"/>

    <path id="finCw145" d="M800 282 a145 145 0 1 1 290 0 a145 145 0 1 1 -290 0"/>
    <path id="finCw153" d="M792 282 a153 153 0 1 1 306 0 a153 153 0 1 1 -306 0"/>
    <path id="finCcw142" d="M803 282 a142 142 0 1 0 284 0 a142 142 0 1 0 -284 0"/>

    <path id="riskCw134" d="M121 665 a134 134 0 1 1 268 0 a134 134 0 1 1 -268 0"/>
    <path id="riskCcw138" d="M117 665 a138 138 0 1 0 276 0 a138 138 0 1 0 -276 0"/>

    <path id="regCw142" d="M800 670 a142 142 0 1 1 284 0 a142 142 0 1 1 -284 0"/>
    <path id="regCw140" d="M802 670 a140 140 0 1 1 280 0 a140 140 0 1 1 -280 0"/>
  </defs>

  <rect class="card" x="38" y="45" width="1124" height="795"/>

  <!-- connectors -->
  <g class="connectors">
    <line class="connector-line" x1="360" y1="330" x2="410" y2="350"/>
    <circle class="connector-dot" cx="410" cy="350" r="7" stroke="var(--orange)"/>
    <line class="connector-line" x1="840" y1="328" x2="787" y2="345"/>
    <circle class="connector-dot" cx="787" cy="345" r="7" stroke="var(--sky)"/>
    <line class="connector-line" x1="360" y1="612" x2="440" y2="575"/>
    <circle class="connector-dot" cx="440" cy="575" r="7" stroke="var(--green)"/>
    <line class="connector-line" x1="850" y1="612" x2="766" y2="568"/>
    <circle class="connector-dot" cx="766" cy="568" r="7" stroke="var(--purple)"/>
  </g>

  <!-- Performance module -->
  <g class="module module--performance">
    <circle class="arc arc--purple" cx="258" cy="268" r="150" stroke-width="42" stroke-dasharray="272.3 9999" transform="rotate(160 258 268)"/>
    <circle class="arc arc--orange" cx="258" cy="268" r="149" stroke-width="40" stroke-dasharray="293.9 9999" transform="rotate(271 258 268)"/>
    <circle class="arc arc--green" cx="258" cy="268" r="131" stroke-width="40" stroke-dasharray="278.9 9999" transform="rotate(30 258 268)"/>
    <text class="arc-label" transform="rotate(212 258 268)"><textPath href="#perfCw143" startOffset="50%">Financial Planning</textPath></text>
    <text class="arc-label" transform="rotate(327 258 268)"><textPath href="#perfCw142" startOffset="50%">Funds Transfer Pricing</textPath></text>
    <text class="arc-label" transform="rotate(91 258 268)"><textPath href="#perfCcw139" startOffset="50%">Business Intelligence</textPath></text>
    <circle class="module-core" cx="258" cy="268" r="107" filter="url(#softShadow)"/>
    <g class="module-icon" aria-hidden="true" transform="translate(-10 0)">
      <path class="icon-stroke" d="M240 236 a32 32 0 1 1 56 0"/>
      <line class="icon-stroke" x1="268" y1="214" x2="268" y2="206"/>
      <line class="icon-stroke" x1="246" y1="222" x2="241" y2="217"/>
      <line class="icon-stroke" x1="290" y1="222" x2="295" y2="217"/>
      <path class="icon-fill" d="M262 234 L282 208 L272 238 Z"/>
      <circle class="icon-fill" cx="267" cy="236" r="5"/>
    </g>
    <text class="module-title" x="260" y="294">PERFORM-</text>
    <text class="module-title" x="260" y="332">ANCE</text>
  </g>

  <!-- Finance module -->
  <g class="module module--finance">
    <circle class="arc arc--orange" cx="945" cy="282" r="152" stroke-width="44" stroke-dasharray="252 9999" transform="rotate(170 945 282)"/>
    <circle class="arc arc--green" cx="945" cy="282" r="160" stroke-width="44" stroke-dasharray="307.2 9999" transform="rotate(272 945 282)"/>
    <circle class="arc arc--sky" cx="945" cy="282" r="135" stroke-width="40" stroke-dasharray="329.9 9999" transform="rotate(25 945 282)"/>
    <text class="arc-label" transform="rotate(217 945 282)"><textPath href="#finCw145" startOffset="50%">Financial Ledgers</textPath></text>
    <text class="arc-label" transform="rotate(327 945 282)"><textPath href="#finCw153" startOffset="50%">Effective Interest Rates</textPath></text>
    <text class="arc-label" transform="rotate(95 945 282)"><textPath href="#finCcw142" startOffset="50%">Hedge Accounting</textPath></text>
    <circle class="module-core" cx="945" cy="282" r="107" filter="url(#softShadow)"/>
    <g class="module-icon" aria-hidden="true">
      <rect class="icon-fill" x="912" y="206" width="38" height="11" rx="5"/>
      <rect class="icon-fill" x="912" y="220" width="38" height="11" rx="5"/>
      <rect class="icon-fill" x="912" y="234" width="38" height="11" rx="5"/>
      <rect class="icon-fill" x="912" y="248" width="38" height="11" rx="5"/>
      <circle class="icon-fill" cx="962" cy="240" r="21"/>
      <circle class="icon-cut" cx="962" cy="240" r="16"/>
      <text x="962" y="249" fill="#ffffff" font-size="24" font-weight="800" text-anchor="middle">$</text>
    </g>
    <text class="module-title" x="945" y="295">FINANCE</text>
  </g>

  <!-- Risk module -->
  <g class="module module--risk">
    <circle class="arc arc--sky" cx="255" cy="665" r="140" stroke-width="48" stroke-dasharray="366.5 9999" transform="rotate(178 255 665)"/>
    <circle class="arc arc--green" cx="255" cy="665" r="130" stroke-width="44" stroke-dasharray="442.4 9999" transform="rotate(340 255 665)"/>
    <text class="arc-label" transform="rotate(245 255 665)"><textPath href="#riskCw134" startOffset="50%">Treasure</textPath></text>
    <text class="arc-label" transform="rotate(70 255 665)"><textPath href="#riskCcw138" startOffset="50%">ALM</textPath></text>
    <circle class="module-core" cx="255" cy="665" r="107" filter="url(#softShadow)"/>
    <g class="module-icon" aria-hidden="true" transform="translate(-28 -15)">
      <path class="icon-stroke" d="M250 646 a36 36 0 1 1 66 0"/>
      <path class="icon-fill" d="M283 612 L309 656 L257 656 Z"/>
      <rect class="icon-cut" x="280" y="626" width="6" height="16" rx="2"/>
      <circle class="icon-cut" cx="283" cy="648" r="3.5"/>
    </g>
    <text class="module-title" x="255" y="690">RISK</text>
  </g>

  <!-- Regulatory module -->
  <g class="module module--regulatory">
    <circle class="arc arc--orange" cx="942" cy="670" r="147" stroke-width="42" stroke-dasharray="297.6 9999" transform="rotate(206 942 670)"/>
    <circle class="arc arc--sky" cx="942" cy="670" r="145" stroke-width="50" stroke-dasharray="283.4 9999" transform="rotate(327 942 670)"/>
    <circle class="arc arc--purple" cx="942" cy="670" r="147" stroke-width="42" stroke-dasharray="292.5 9999" transform="rotate(86 942 670)"/>
    <text class="arc-label" transform="rotate(265 942 670)"><textPath href="#regCw142" startOffset="50%">Texation Reporting</textPath></text>
    <text class="arc-label" transform="rotate(22 942 670)"><textPath href="#regCw140" startOffset="50%">FSCS SCV</textPath></text>
    <text class="arc-label" transform="rotate(143 942 670)"><textPath href="#regCw142" startOffset="50%">Regulatory Reaporting</textPath></text>
    <circle class="module-core" cx="942" cy="670" r="107" filter="url(#softShadow)"/>
    <g class="module-icon" aria-hidden="true" transform="translate(12 -8)">
      <path class="icon-fill" d="M904 600 h28 l14 14 v40 h-42 Z"/>
      <rect class="icon-cut" x="912" y="624" width="22" height="3"/>
      <rect class="icon-cut" x="912" y="633" width="16" height="3"/>
      <path class="icon-fill" d="M950 630 l18 7 v12 c0 10 -8 16 -18 20 c-10 -4 -18 -10 -18 -20 v-12 Z" stroke="var(--core-light)" stroke-width="3"/>
      <path d="M943 649 l5 5 l9 -10" fill="none" stroke="var(--core-light)" stroke-width="3" stroke-linecap="round" stroke-linejoin="round"/>
    </g>
    <text class="module-title" x="942" y="692">REGULAT-</text>
    <text class="module-title" x="942" y="730">ORY</text>
  </g>

  <!-- Shared data hub -->
  <g class="hub">
    <circle class="hub-ring" cx="600" cy="440" r="215"/>
    <circle class="hub-dots" cx="600" cy="440" r="198"/>
    <circle class="hub-core" cx="600" cy="440" r="180" filter="url(#softShadow)"/>
    <g class="exchange-mark" role="img" aria-label="Icon of two hands passing a data sheet between them">
      <rect x="548" y="322" width="106" height="106" rx="4" transform="rotate(-4 601 375)"/>
    </g>
    <text class="hub-title" x="600" y="530">SHARED</text>
    <text class="hub-title" x="600" y="580">DATA</text>
  </g>
</svg>
</body>
</html>
```